Brochure Design - Non-Profit Fundraising Stream

We are a non-profit organization that is developing a fundraising project through the donation of life insurance policies. We have three brochures in each English and French that we developed for a sister organization that we want to reintegrate with our Foundation, keeping the same copy text just changing the logos, colors and make it overall more visually appealing. The foundation is called the 'Varnek-Holt Syndrome Foundation Canada'.
The original files in .docx format are attached as is the full logo and two symbol files. The deliverables would be six documents in total (InDesign or .docx), each brochure in English and French. The color hex codes are:
red: #7b2850
dark blue: #2c79a7
pale blue: #78b2e2

```html
<!DOCTYPE html>
<html lang="en">
<head>
<meta charset="utf-8">
<title>Varnek-Holt Syndrome Foundation Canada – Donor Brochure</title>
<link href="https://fonts.googleapis.com/css2?family=Oswald:wght@500;600&family=Open+Sans:wght@400;600;700&display=swap" rel="stylesheet">
<style>
  :root{
    --red:#7b2850;
    --blue:#2c79a7;
    --pale:#78b2e2;
    --ink:#5f6770;
    --paper:#ffffff;
    --backdrop:#e3e3e3;
  }
  *{box-sizing:border-box;margin:0;padding:0}
  html,body{width:1200px;height:900px;overflow:hidden}
  body{background:var(--backdrop);font-family:"Open Sans",Arial,sans-serif;color:var(--ink);position:relative}
  .sheet{position:absolute;top:114px;width:520px;height:672px;background:var(--paper);box-shadow:0 2px 10px rgba(0,0,0,.12);padding:36px 38px}
  .sheet--front{left:60px}
  .sheet--back{left:620px}
  .heading{font-family:"Oswald",Arial,sans-serif;font-weight:600;color:var(--blue);text-transform:uppercase;letter-spacing:.04em;text-align:center;font-size:14px}
  .body-text{font-size:8.5px;line-height:1.65}
  .heart-list{list-style:none}
  .heart-list li{font-size:8.5px;line-height:1.6;padding-left:16px;position:relative;margin-bottom:7px}
  .heart-list li::before{content:"\2665";color:var(--red);position:absolute;left:0;top:0;font-size:9px}

  /* front */
  .front-top{display:flex;justify-content:space-between}
  .front-intro{width:230px}
  .brand{display:flex;align-items:center;gap:8px;margin-bottom:26px}
  .brand__mark{width:14px;height:14px;border-radius:50%;background:var(--pale);flex:none}
  .brand__name{font-weight:600;color:var(--blue);font-size:15px;line-height:1.2}
  .audience{width:196px}
  .audience__label{font-family:"Oswald",Arial,sans-serif;font-weight:500;color:var(--red);font-size:11px;letter-spacing:.06em;text-align:right;margin-bottom:8px}
  .audience__label span{margin-left:4px}
  .photo{height:108px;border:3px solid var(--pale);background:linear-gradient(135deg,#f4f6f9,#dfe8f2 55%,#c9d9ea)}
  .policies{margin-top:34px}
  .policies__grid{display:flex;justify-content:space-between;margin-top:18px}
  .policy{width:100px;text-align:center}
  .policy svg{width:34px;height:34px;display:block;margin:0 auto 8px}
  .policy__caption{font-size:8px;font-weight:700;color:var(--blue);line-height:1.35}
  .advantages{margin-top:44px}
  .advantages .heart-list{margin-top:18px}

  /* back */
  .independence .heart-list{margin-top:16px}
  .process{margin-top:34px}
  .steps{position:relative;height:170px;margin-top:10px}
  .step{position:absolute;width:84px}
  .step__num{width:30px;height:30px;border-radius:50%;border:3px solid currentColor;background:#fff;font-family:"Oswald",Arial,sans-serif;font-weight:600;font-size:12px;display:flex;align-items:center;justify-content:center;margin-left:12px}
  .step__stem{width:3px;height:10px;background:currentColor;margin-left:25px}
  .step__box{height:62px;border-radius:8px;background:currentColor;padding:9px 8px;display:flex;align-items:center}
  .step__box span{color:#fff;font-size:7.5px;line-height:1.35;font-weight:600}
  .step--red{color:var(--red)}
  .step--blue{color:var(--blue)}
  .step--pale{color:var(--pale)}
  .disclosure{margin-top:22px}
  .disclosure .heart-list{margin-top:16px}
  .contact{margin-top:18px;text-align:right}
  .contact__phone{font-family:"Oswald",Arial,sans-serif;font-weight:600;color:var(--ink);font-size:12px;letter-spacing:.03em}
  .contact__web{font-size:8px;color:var(--red);margin-top:3px}
</style>
</head>
<body>

<section class="sheet sheet--front">
  <div class="front-top">
    <div class="front-intro">
      <div class="brand">
        <span class="brand__mark"></span>
        <span class="brand__name">Varnek-Holt Syndrome<br>Foundation Canada</span>
      </div>
      <p class="body-text">You can maintain or substantially increase your financial contribution to the Foundation by donating a life insurance policy you no longer need. Every year, thousands of Canadians let valuable policies lapse. A donated policy can provide a meaningful gift today, with a tax receipt for its fair market value, while the Foundation receives the full benefit later.</p>
    </div>
    <div class="audience">
      <p class="audience__label">FOR DONORS<span>&#9829; &#9829;</span></p>
      <div class="photo" role="img" aria-label="Photo of a smiling woman holding a balloon"></div>
    </div>
  </div>

  <div class="policies">
    <h2 class="heading">Suitable Policies</h2>
    <div class="policies__grid">
      <div class="policy">
        <svg viewBox="0 0 34 34"><rect x="7" y="4" width="20" height="26" rx="2" fill="none" stroke="#2c79a7" stroke-width="2.5"/><path d="M11 11h12M11 16h12M11 21h8" stroke="#2c79a7" stroke-width="2"/></svg>
        <p class="policy__caption">Term, Whole life, Universal or term-to-100 policies</p>
      </div>
      <div class="policy">
        <svg viewBox="0 0 34 34"><circle cx="17" cy="11" r="6" fill="#2c79a7"/><path d="M6 30c0-7 5-11 11-11s11 4 11 11z" fill="#2c79a7"/></svg>
        <p class="policy__caption">Insured lives over 70 years old</p>
      </div>
      <div class="policy">
        <svg viewBox="0 0 34 34"><path d="M17 3l11 4v9c0 7-5 12-11 15C11 28 6 23 6 16V7z" fill="#2c79a7"/><path d="M12 17l4 4 7-8" stroke="#fff" stroke-width="2.5" fill="none"/></svg>
        <p class="policy__caption">In force greater than 3 years</p>
      </div>
      <div class="policy">
        <svg viewBox="0 0 34 34"><path d="M4 13L17 5l13 8z" fill="#2c79a7"/><path d="M8 15v10M14 15v10M20 15v10M26 15v10" stroke="#2c79a7" stroke-width="3"/><rect x="4" y="27" width="26" height="3" fill="#2c79a7"/></svg>
        <p class="policy__caption">Minimum death benefit of $50,000</p>
      </div>
    </div>
  </div>

  <div class="advantages">
    <h2 class="heading">Advantages of Donating a Life Insurance Policy</h2>
    <ul class="heart-list">
      <li>You obtain a tax receipt equal to the fair market value of the policy transferred to the Foundation.</li>
      <li>You convert an unneeded or costly policy into a lasting gift.</li>
      <li>Eliminate the burden of annual premium payments.</li>
      <li>The Foundation becomes owner and beneficiary, and funds premiums until the benefit is paid at maturity.</li>
    </ul>
  </div>
</section>

<section class="sheet sheet--back">
  <div class="independence">
    <h2 class="heading">Maintain Financial Independence</h2>
    <ul class="heart-list">
      <li>Your policy can be reviewed to keep coverage that still meets your family's needs.</li>
      <li>Premiums saved remain available for your retirement and other priorities.</li>
      <li>Reduce or avoid estate taxes.</li>
    </ul>
  </div>

  <div class="process">
    <h2 class="heading">Donation Process</h2>
    <div class="steps">
      <div class="step step--red" style="left:6px;top:68px"><div class="step__num">01</div><div class="step__stem"></div><div class="step__box"><span>Contact the Foundation to discuss your policy</span></div></div>
      <div class="step step--blue" style="left:94px;top:51px"><div class="step__num">02</div><div class="step__stem"></div><div class="step__box"><span>Policy review and valuation</span></div></div>
      <div class="step step--pale" style="left:182px;top:34px"><div class="step__num">03</div><div class="step__stem"></div><div class="step__box"><span>Transfer of ownership completed</span></div></div>
      <div class="step step--red" style="left:270px;top:17px"><div class="step__num">04</div><div class="step__stem"></div><div class="step__box"><span>Tax receipt issued to donor</span></div></div>
      <div class="step step--blue" style="left:358px;top:0"><div class="step__num">05</div><div class="step__stem"></div><div class="step__box"><span>Foundation manages the policy</span></div></div>
    </div>
  </div>

  <div class="disclosure">
    <h2 class="heading">Disclosure</h2>
    <ul class="heart-list">
      <li>The Foundation recommends that donors consult an independent financial or legal advisor before transferring ownership of any life insurance policy.</li>
      <li>A change of ownership may trigger a taxable disposition; the value of the gift is determined by a qualified appraiser at the time of transfer.</li>
      <li>Donations are final and cannot be reversed once the policy is transferred.</li>
    </ul>
    <div class="contact">
      <p class="contact__phone">CALL US: 1 (800) 555-0147</p>
      <p class="contact__web">varnekholtfoundation.ca</p>
    </div>
  </div>
</section>

</body>
</html>
```